Update CORVEL Worldwide's Website

We need to update our current website - www.corvelworldwide-example.com, either with the same template (Joomla 1.5 CMS site using the Pixelforge Horizon) or new one. Please see the first Attached File for additional details of the changes we would like.

A brief summary of changes are:
- Change colors and update the tagline on the logo
- Remove text and add text and pictures
- Remove pages and add a page
and other minor changes

The site is currently hosted at Net Pallow. You will have access to the FTP file transfer to download and work with the current files.

Please contact me with any questions: derek@corvelworldwide-example.com
Updates

Project Deadline Extended
Reason: Extending to view additional designs. Please indicate if you are proposing a completely new site or redo of the current template. Best, Derek

```html
<!DOCTYPE html>
<html lang="en">
<head>
<meta charset="utf-8">
<title>QUORVANE Worldwide — Affordable Housing &amp; Social Investments</title>
<link href="https://fonts.googleapis.com/css2?family=Open+Sans:ital,wght@0,400;0,600;1,400&display=swap" rel="stylesheet">
<style>
:root{
  --blue:#2b74c2;
  --blue-dark:#1f5fa8;
  --nav-top:#3f8bd6;
  --nav-bottom:#2466b3;
  --orange:#f7931e;
  --orange-light:#fdc04e;
  --text:#4a4a4a;
  --muted:#8a8a8a;
  --line:#e3e3e3;
  --footer:#f4f4f4;
}
*{margin:0;padding:0;box-sizing:border-box}
html,body{width:1003px;height:1200px;overflow:hidden;background:#fff}
body{font-family:'Open Sans',Arial,sans-serif;color:var(--text);position:relative}
.abs{position:absolute}

.header-band{left:0;top:107px;width:1003px;height:44px;background:linear-gradient(#f3f3f3,#fafafa);border-bottom:1px solid var(--line)}
.brand{left:64px;top:38px;display:flex;align-items:center;gap:8px}
.brand-dot{width:22px;height:22px;border-radius:50%;background:var(--blue)}
.brand-name{font-size:29px;font-weight:600;color:var(--blue);letter-spacing:-.5px;line-height:1}
.tagline{left:105px;top:69px;font-size:13.5px;font-style:italic;color:#8a8a8a}

.lang{left:834px;top:64px;width:97px;height:27px;border:1px solid #d8d8d8;border-radius:2px;background:#fff;display:flex;align-items:center;padding-left:9px;font-size:12px;color:#333}
.lang-flag{width:18px;height:12px;background:#2c4f9e;margin-right:7px}
.lang-caret{margin-left:7px;width:0;height:0;border-left:5px solid transparent;border-right:5px solid transparent;border-top:6px solid #555}

.main-nav{left:64px;top:107px;width:875px;height:44px;display:flex;background:linear-gradient(var(--nav-top),var(--nav-bottom))}
.main-nav a{color:#fff;text-decoration:none;font-size:13px;text-transform:uppercase;display:flex;align-items:center;justify-content:center;border-right:1px solid rgba(255,255,255,.18);letter-spacing:.2px}
.main-nav a.active{background:#1e5ca4}

.hero{left:64px;top:151px;width:875px;height:333px;overflow:hidden;border-radius:0 0 3px 3px}
.hero-photo{position:absolute;left:0;top:0;width:875px;height:333px;background:linear-gradient(100deg,#e6e4e0 0%,#f2f1ee 35%,#bcd6ea 60%,#c9b99c 85%,#a9a394 100%)}
.hero-panel{position:absolute;left:0;top:0}
.hero-copy{position:absolute;left:649px;top:72px;width:215px;color:#fff}
.hero-title{font-size:22px;font-weight:400;line-height:1.2}
.hero-sub{font-size:11px;font-weight:600;margin-top:6px}
.hero-text{font-size:11px;line-height:19px;margin-top:6px}
.hero-dots{display:flex;gap:3px;margin-top:14px}
.hero-dots span{width:11px;height:11px;border-radius:50%;background:#fff}

h2.section-title{font-weight:400;color:var(--blue);font-size:26px;line-height:1}
.welcome{left:64px;top:517px;width:575px}
.welcome p{font-size:11px;line-height:17px;margin-top:8px}
.welcome p.gap{margin-top:17px}

.feature-img{left:681px;top:508px;width:258px;height:120px;background:linear-gradient(#9bb17a,#b9b6ac 55%,#8f8c84);border:1px solid #d6d6d6}
.feature-title{left:682px;top:636px;font-size:20.5px;line-height:22px;color:var(--orange);font-weight:400}
.feature-text{left:682px;top:684px;width:250px;font-size:10.5px;line-height:17.5px;color:var(--muted)}

.divider{left:64px;top:769px;width:875px;height:1px;background:linear-gradient(90deg,transparent,var(--line) 15%,var(--line) 85%,transparent)}

.card{top:807px;width:266px}
.card-img{width:266px;height:103px;border:1px solid #d6d6d6}
.card-title{font-size:20px;font-weight:400;color:#444;margin-top:10px}
.card-text{font-size:10.5px;line-height:17px;color:var(--muted);margin-top:4px}
.btn{display:inline-block;margin-top:10px;width:107px;height:31px;line-height:31px;text-align:center;color:#fff;font-size:11.5px;text-transform:uppercase;text-decoration:none;border-radius:2px;background:linear-gradient(#3d86d1,var(--blue-dark));box-shadow:0 1px 2px rgba(0,0,0,.25)}

.office{left:681px;top:799px;width:260px}
.office h3{font-size:13px;font-weight:400;color:#333;margin-top:8px}
.office p{font-size:10.5px;line-height:17.8px;color:#666}
.office .us{margin-top:12px}

.footer{left:0;top:1099px;width:1003px;height:101px;background:var(--footer);border-top:1px solid #dcdcdc}
.footer-nav{left:65px;top:1126px;font-size:12px;color:#444}
.footer-nav span{margin:0 5px}
.copyright{left:65px;top:1151px;font-size:11px;color:#555}
.social{left:852px;top:1123px;display:flex;gap:10px}
.social span{width:21px;height:21px;border-radius:2px}
</style>
</head>
<body>

<div class="abs header-band"></div>

<div class="abs brand"><span class="brand-dot"></span><span class="brand-name">QUORVANE Worldwide</span></div>
<div class="abs tagline">Affordable Housing &amp; Social Investments</div>

<div class="abs lang"><span class="lang-flag"></span>English<span class="lang-caret"></span></div>

<nav class="abs main-nav">
  <a class="active" style="width:97px">Home</a>
  <a style="width:223px">Community Development</a>
  <a style="width:191px">Affordable Housing</a>
  <a style="width:179px">Alternative Energy</a>
  <a style="width:185px;border-right:0">Quorvane Team</a>
</nav>

<section class="abs hero">
  <div class="hero-photo" role="img" aria-label="Bright apartment interior with kitchen, dining chairs, sofa and large windows overlooking the city and sea"></div>
  <svg class="hero-panel" width="875" height="333" viewBox="0 0 875 333">
    <defs>
      <linearGradient id="panelFill" x1="0" y1="0" x2="0" y2="1">
        <stop offset="0" stop-color="#fdc04e"/>
        <stop offset="1" stop-color="#f7931e"/>
      </linearGradient>
    </defs>
    <path d="M642 0 C 610 50, 605 110, 622 170 C 640 235, 630 290, 628 333 L875 333 L875 0 Z" fill="#fff"/>
    <path d="M647 0 C 615 50, 610 110, 627 170 C 645 235, 635 290, 633 333 L875 333 L875 0 Z" fill="url(#panelFill)"/>
  </svg>
  <div class="hero-copy">
    <h1 class="hero-title">PH MAREA PROJECT</h1>
    <div class="hero-sub">SED METUS AUGUE CONVALLIS</div>
    <p class="hero-text">Aliquam nec erat at purus cursus interdum Vestibulum ligula augue bibendum accumsan vestibulum ut commodo a mi Morbi</p>
    <div class="hero-dots"><span></span><span></span><span></span><span></span></div>
  </div>
</section>

<section class="abs welcome">
  <h2 class="section-title">Welcome to QUORVANE Worldwide</h2>
  <p style="margin-top:12px">QUORVANE is a socially responsible corporation working in affordable housing and alternative energy.</p>
  <p>We at QUORVANE think environmental and social accountability are as fundamental as making a profit. In fact, they go hand in hand. All our projects— affordable green housing —specialize in superior investment and ownership opportunities and employ the latest in sustainable and green technologies.</p>
  <p class="gap">Our vision is to create and support eco-friendly, sustainable property developments in Panama that maximize profit for our investors and strengthen communities for our neighbors.</p>
  <p class="gap">QUORVANE Worldwide: the next generation of sustainable real estate development in Panama.</p>
</section>

<div class="abs feature-img" role="img" aria-label="Two-storey grey family house with trees behind"></div>
<h3 class="abs feature-title">Affordable Housing<br>Innovation</h3>
<p class="abs feature-text">Malesuada nec ultricies sit amet porttitor mattis enim In massa libero interdum nec interdum v</p>

<div class="abs divider"></div>

<article class="abs card" style="left:64px">
  <div class="card-img" role="img" aria-label="Modern apartment buildings with a green panelled facade" style="background:linear-gradient(90deg,#e4e6e8 0%,#d9dde0 40%,#7ccc2e 48%,#4fae24 60%,#e6e8ea 70%,#dfe3e6 100%)"></div>
  <h3 class="card-title">Community Development</h3>
  <p class="card-text">Aliquam nec erat at purus cursus interdum Vestibu-lum ligula augue bibendum accumsan vestibulum ut commodo a mi Morbi ornare gravida</p>
  <a class="btn">Read More</a>
</article>

<article class="abs card" style="left:360px">
  <div class="card-img" role="img" aria-label="Rooftop terrace with tables overlooking the city skyline and sea" style="background:linear-gradient(#9fc3e0 0%,#c9d9e4 25%,#b7a98c 45%,#cfc3b0 75%,#a39a8c 100%)"></div>
  <h3 class="card-title">Social Investment</h3>
  <p class="card-text">Aliquam nec erat at purus cursus interdum Vestibu-lum ligula augue bibendum accumsan vestibulum ut commodo a mi Morbi ornare gravida</p>
  <a class="btn">Read More</a>
</article>

<section class="abs office">
  <h2 class="section-title" style="font-size:23.5px">Office Details</h2>
  <h3 style="margin-top:10px">QUORVANE Panama, S.A.</h3>
  <p>Panama Office<br>Los Robles, Plaza Comercial Miramar, #22<br>Panama City, Panama<br>Ofc: 507-555-0136 Fax: 507-555-0117<br>contact@quorvane-example.com</p>
  <h3 class="us">U.S. Office</h3>
  <p>415 Harbor Lane, #310<br>Seattle, WA 98101<br>Ofc: 202-555-0147<br>Fax: 703-555-0139</p>
</section>

<footer class="abs footer"></footer>
<nav class="abs footer-nav">Home<span>/</span>Community Development<span>/</span>Affordable Housing<span>/</span>Alternative Energy<span>/</span>QUORVANE Team</nav>
<div class="abs copyright">© 2014 Company Name&nbsp; All right reserved&nbsp; Term of Use</div>
<div class="abs social" aria-label="Social links">
  <span style="background:#3b5b9a"></span>
  <span style="background:#3fb4e6"></span>
  <span style="background:#1f6fb0"></span>
</div>

</body>
</html>
```